Fundraiser Flyer and Email Template

We are looking for a flexible coordinated flyer and email template. The feel of both should be more formal or professional. We are not looking for an overly "political" design that features American flags or other "political" symbols.

We are a political fundraising firm that works with elected officials to set up fundraisers for their campaigns. We send the invites to these events via US Mail and email, so we are looking for a standardized template that will work as both an 8.5 x 11 inch printed flyer, as well as an email template.

The information in the email will be text, but images can be used for formatting.

Some clients have a campaign logo, others do not. The format should be flexible enough to either include the logo, or leave it out. Size also varies.

Any colors in the template should be editable so we can match logos as we get them.

We're open to any format that allows us to edit the format as needed. This would include Photoshop, Microsoft Word, etc.

The text of the invite should include space for:

---------------------------------------
NAME
DISTRICT NUMBER AND OFFICE

DATE OF EVENT
TIME OF EVENT

LOCATION
LOCATION ADDRESS
LOCATION CITY, STATE, ZIP

SUGGESTED CONTRIBUTION LEVELS (Typically 3 levels are provided such as Gold: $1,000, Silver: $500, Bronze: $250)

ADDRESS TO SEND CHECKS TO

RSVP CONTACT INFORMATION

The invite will also need fine-print at the bottom that reads:
"Pennsylvania law allows personal, partnership, and PAC contributions. By law we cannot accept corporate contributions
Paid for by [NAME]"

Industry/Entity Type

It Professional

Font styles to use
Serif
Sans Serif

Requirements
Must have
• Must have spaces for:
• NAME
• DISTRICT NUMBER AND OFFICE
• DATE OF EVENT
• TIME OF EVENT
• LOCATION
• LOCATION ADDRESS
• LOCATION CITY, STATE, ZIP
• SUGGESTED CONTRIBUTION LEVELS (Typically 3 levels are provided such as Gold: $1,000, Silver: $500, Bronze: $250)
• ADDRESS TO SEND CHECKS TO
• RSVP CONTACT INFORMATION
• The invite will also need fine-print at the bottom that reads:
• "Pennsylvania law allows personal, partnership, and PAC contributions. By law we cannot accept corporate contributions
• Paid for by [NAME]"
Should not have
• It should not be overly "political".

```html
<!DOCTYPE html>
<html lang="en">
<head>
<meta charset="utf-8">
<title>Fundraiser Flyer Template – Colour Variants</title>
<link rel="stylesheet" href="https://fonts.googleapis.com/css2?family=Montserrat:wght@400;500&family=Oswald:wght@300;400&display=swap">
<style>
  :root {
    --canvas-bg: #e0e0e0;
    --panel-fill: rgba(255, 255, 255, 0.78);
    --field-fill: #ffffff;
    --field-shadow: rgba(0, 0, 0, 0.28);
    --label-ink: #2b2b2b;
    --headline-ink: #ffffff;
    --footer-bg: #000000;
    --footer-ink: #e8e8e8;
    --logo-fill: rgba(255, 255, 255, 0.38);
  }
  * { box-sizing: border-box; margin: 0; padding: 0; }
  html, body { width: 1200px; height: 900px; overflow: hidden; background: var(--canvas-bg); }
  body { position: relative; font-family: "Montserrat", Arial, sans-serif; }

  .flyer {
    position: absolute; top: 20px; width: 570px; height: 737px; overflow: hidden;
  }
  .flyer--slate { left: 20px; --overlay-a: #4e4f55; --overlay-b: #7d7e84; --overlay-c: #a9a9ae; --mic-tone: #8c8c90; }
  .flyer--crimson { left: 610px; --overlay-a: #b9433a; --overlay-b: #d26650; --overlay-c: #e89a86; --mic-tone: #d88a70;
    --panel-fill: rgba(255, 245, 242, 0.8); }

  .flyer__backdrop {
    position: absolute; inset: 0 0 54px 0;
    background:
      radial-gradient(circle at 55px 290px, var(--mic-tone) 0 125px, transparent 126px),
      radial-gradient(ellipse at 70% 45%, var(--overlay-c) 0%, transparent 60%),
      linear-gradient(160deg, var(--overlay-a) 0%, var(--overlay-b) 55%, var(--overlay-a) 100%);
  }

  .logo-placeholder {
    position: absolute; left: 37px; top: 38px; width: 146px; height: 146px; border-radius: 50%;
    background: var(--logo-fill); color: #fff; display: flex; align-items: center; justify-content: center;
    text-align: center; font-family: "Montserrat", Arial, sans-serif; font-weight: 400;
    font-size: 30px; line-height: 38px; letter-spacing: 1px;
  }

  .side-note {
    position: absolute; left: 35px; top: 426px; width: 175px;
    font-family: "Oswald", "Arial Narrow", sans-serif; font-weight: 300; color: var(--headline-ink);
    font-size: 17px; line-height: 20px;
  }
  .side-headline {
    position: absolute; left: 35px; top: 535px; width: 180px;
    font-family: "Oswald", "Arial Narrow", sans-serif; font-weight: 300; color: var(--headline-ink);
    font-size: 27px; line-height: 32px; text-transform: uppercase;
  }

  .invite-panel {
    position: absolute; left: 220px; top: 36px; width: 317px; height: 636px;
    border-radius: 12px; background: var(--panel-fill); padding: 19px 28px 0 26px;
  }
  .field-group { margin-bottom: 9px; }
  .field-group--wide-gap { margin-bottom: 15px; }
  .field-label {
    display: block; height: 14px; line-height: 14px; margin-bottom: 7px;
    font-size: 11px; color: var(--label-ink); letter-spacing: 0.3px; text-transform: uppercase;
  }
  .field-input {
    height: 24px; width: 262px; margin-left: 1px; background: var(--field-fill);
    box-shadow: 2px 2px 2px var(--field-shadow);
  }
  .field-input + .field-input { margin-top: 10px; }
  .field-row { display: flex; gap: 24px; }
  .field-row .field-group { width: 119px; }
  .field-row .field-input { width: 119px; }

  .level-options { display: flex; gap: 0; height: 26px; margin-left: 1px; }
  .level { display: flex; align-items: flex-start; width: 76px; }
  .level:last-child { width: auto; }
  .level__box { width: 26px; height: 26px; background: var(--field-fill); box-shadow: 2px 2px 2px var(--field-shadow); flex: none; }
  .level__text { margin-left: 7px; margin-top: 2px; color: var(--label-ink); font-size: 11px; line-height: 11px; }
  .level__amount { display: block; font-size: 7px; line-height: 9px; }

  .fine-print {
    position: absolute; left: 0; bottom: 0; width: 570px; height: 54px; background: var(--footer-bg);
    color: var(--footer-ink); font-size: 10.5px; line-height: 13px; padding: 8px 28px 0 28px;
  }
</style>
</head>
<body>

  <section class="flyer flyer--slate">
    <div class="flyer__backdrop" role="img" aria-label="Blurred event photo with a stage microphone, slate colour overlay"></div>
    <div class="logo-placeholder">LOGO<br>HERE</div>
    <p class="side-note">Background overlay color can be changed according to logo color.</p>
    <p class="side-headline">Any text, images or titles can be added here</p>
    <div class="invite-panel">
      <div class="field-group"><span class="field-label">Name:</span><div class="field-input"></div></div>
      <div class="field-group"><span class="field-label">District number and office:</span><div class="field-input"></div></div>
      <div class="field-row">
        <div class="field-group"><span class="field-label">Date of event:</span><div class="field-input"></div></div>
        <div class="field-group"><span class="field-label">Time of event:</span><div class="field-input"></div></div>
      </div>
      <div class="field-group"><span class="field-label">Location:</span><div class="field-input"></div></div>
      <div class="field-group field-group--wide-gap"><span class="field-label">Location address:</span><div class="field-input"></div><div class="field-input"></div></div>
      <div class="field-group"><span class="field-label">Location city, state, zip:</span><div class="field-input"></div></div>
      <div class="field-group" style="margin-bottom:14px"><span class="field-label">Suggested contribution levels:</span>
        <div class="level-options">
          <div class="level"><div class="level__box"></div><div class="level__text">GOLD<span class="level__amount">($1,000)</span></div></div>
          <div class="level"><div class="level__box"></div><div class="level__text">Silver<span class="level__amount">($500)</span></div></div>
          <div class="level"><div class="level__box"></div><div class="level__text">Bronze<span class="level__amount">($250)</span></div></div>
        </div>
      </div>
      <div class="field-group field-group--wide-gap"><span class="field-label">Address to send checks to:</span><div class="field-input"></div><div class="field-input"></div></div>
      <div class="field-group"><span class="field-label">RSVP contact information:</span><div class="field-input"></div><div class="field-input"></div></div>
    </div>
    <footer class="fine-print">Pennsylvania law allows personal, partnership, and PAC contributions. By law we cannot accept corporate contributions - Paid for by [NAME]</footer>
  </section>

  <section class="flyer flyer--crimson">
    <div class="flyer__backdrop" role="img" aria-label="Blurred event photo with a stage microphone, crimson colour overlay"></div>
    <div class="logo-placeholder">LOGO<br>HERE</div>
    <p class="side-note">Background overlay color can be changed according to logo color.</p>
    <p class="side-headline">Any text, images or titles can be added here</p>
    <div class="invite-panel">
      <div class="field-group"><span class="field-label">Name:</span><div class="field-input"></div></div>
      <div class="field-group"><span class="field-label">District number and office:</span><div class="field-input"></div></div>
      <div class="field-row">
        <div class="field-group"><span class="field-label">Date of event:</span><div class="field-input"></div></div>
        <div class="field-group"><span class="field-label">Time of event:</span><div class="field-input"></div></div>
      </div>
      <div class="field-group"><span class="field-label">Location:</span><div class="field-input"></div></div>
      <div class="field-group field-group--wide-gap"><span class="field-label">Location address:</span><div class="field-input"></div><div class="field-input"></div></div>
      <div class="field-group"><span class="field-label">Location city, state, zip:</span><div class="field-input"></div></div>
      <div class="field-group" style="margin-bottom:14px"><span class="field-label">Suggested contribution levels:</span>
        <div class="level-options">
          <div class="level"><div class="level__box"></div><div class="level__text">GOLD<span class="level__amount">($1,000)</span></div></div>
          <div class="level"><div class="level__box"></div><div class="level__text">Silver<span class="level__amount">($500)</span></div></div>
          <div class="level"><div class="level__box"></div><div class="level__text">Bronze<span class="level__amount">($250)</span></div></div>
        </div>
      </div>
      <div class="field-group field-group--wide-gap"><span class="field-label">Address to send checks to:</span><div class="field-input"></div><div class="field-input"></div></div>
      <div class="field-group"><span class="field-label">RSVP contact information:</span><div class="field-input"></div><div class="field-input"></div></div>
    </div>
    <footer class="fine-print">Pennsylvania law allows personal, partnership, and PAC contributions. By law we cannot accept corporate contributions - Paid for by [NAME]</footer>
  </section>

</body>
</html>
```